Crestline Pools New website

I currently operate a swimming pool service and repair business and looking for a re design for my website as it has been over 5 years since it was designed. current site is crestlinepoolsqv.com

```html
<!DOCTYPE html>
<html lang="en">
<head>
<meta charset="utf-8">
<title>Crestline Pools</title>
<link rel="stylesheet" href="https://fonts.googleapis.com/css2?family=Poppins:wght@400;500;600;700&display=swap">
<style>
:root{
  --blue:#0f5a9c;
  --blue-deep:#0a4589;
  --blue-water:#1a6fc0;
  --orange:#f7941d;
  --orange-light:#fdb243;
  --text:#3a3a3a;
  --night:#1b2a3d;
  --white:#ffffff;
}
*{box-sizing:border-box;margin:0;padding:0}
html,body{width:1200px;height:4823px;overflow:hidden}
body{position:relative;background:var(--white);font-family:'Poppins',sans-serif;color:var(--text)}
.abs{position:absolute}
.photo{position:absolute}
.btn{position:absolute;display:flex;align-items:center;justify-content:center;width:194px;height:52px;border-radius:26px;background:linear-gradient(180deg,var(--orange-light),var(--orange));color:var(--white);font-weight:600;font-size:15px;letter-spacing:.5px;text-transform:uppercase;text-decoration:none}
.heading{position:absolute;text-align:center;color:var(--blue);font-weight:500;font-size:38px;line-height:41px}
.heading .lead{color:#333}
.copy{position:absolute;text-align:center;font-size:14.5px;line-height:26.5px;color:var(--text)}
.copy p+p{margin-top:6px}
.accent{position:absolute;width:124px;height:124px;background:linear-gradient(135deg,var(--blue) 0 50%,var(--orange) 50% 100%)}

/* header */
.hero{position:absolute;left:0;top:0;width:1200px;height:721px;background:linear-gradient(180deg,#1c2f4d 0%,#2b4568 38%,#3c5a6c 62%,#1f5764 80%,#183946 100%)}
.nav{position:absolute;top:36px;display:flex;gap:42px;font-size:14px;color:var(--white);text-transform:uppercase}
.nav a{color:inherit;text-decoration:none}
.nav .active{color:var(--orange)}
.nav-rule{position:absolute;top:82px;height:1px;background:rgba(255,255,255,.55)}
.brand{position:absolute;display:flex;align-items:center;gap:8px;font-weight:600;font-size:22px;white-space:nowrap}
.brand .dot{width:18px;height:18px;border-radius:50%;background:var(--orange)}
.estimate-tab{position:absolute;left:983px;top:26px;width:144px;height:40px;background:var(--orange);color:var(--white);font-size:13.5px;display:flex;align-items:center;justify-content:center;text-transform:uppercase}
.hero-title{position:absolute;left:0;top:285px;width:1200px;text-align:center;color:var(--white);font-weight:700;font-size:68px;line-height:72px;text-shadow:0 2px 8px rgba(0,0,0,.35)}

.diamond{position:absolute;width:362px;height:362px;border-radius:22px;transform:rotate(45deg);background:linear-gradient(135deg,#3aa0d8,#1a6bb0)}
.water-panel{position:absolute;background:linear-gradient(160deg,#0b5fae,#0a3f84)}

/* contact */
.contact{position:absolute;left:0;top:3963px;width:1200px;height:539px;background:linear-gradient(180deg,#1a2433,#24354a 60%,#1a2838)}
.field{position:absolute;height:48px;border-radius:24px;background:var(--white);font-size:12px;color:#555;padding:16px 24px}
.field.message{height:112px;border-radius:22px}
.contact-line{position:absolute;left:0;top:4080px;width:1200px;display:flex;justify-content:center;gap:18px;color:var(--white);font-size:18px;align-items:center}
.contact-line span{display:flex;align-items:center;gap:12px}

/* footer */
.footer-nav{position:absolute;top:4606px;display:flex;gap:42px;font-size:14px;color:#333;text-transform:uppercase}
.social{position:absolute;left:513px;top:4745px;display:flex;gap:16px}
.social span{width:22px;height:22px;border-radius:50%;background:#222}
</style>
</head>
<body>

<!-- Header / hero -->
<section class="hero" role="img" aria-label="Modern house with a curved illuminated swimming pool at dusk"></section>
<nav class="nav" style="left:84px"><a class="active">Home</a><a>About Us</a><a>Services</a></nav>
<div class="nav-rule" style="left:75px;width:420px"></div>
<div class="brand" style="left:512px;top:66px;color:var(--white)"><span class="dot"></span>Crestline Pools</div>
<nav class="nav" style="left:765px"><a>Why Us</a><a>Contact Us</a></nav>
<div class="nav-rule" style="left:705px;width:420px"></div>
<div class="estimate-tab">Free Estimate</div>
<h1 class="hero-title">Reliable pool Service<br>you can Count on</h1>
<a class="btn" style="left:472px;top:457px;width:256px;height:56px;border-radius:28px;font-size:20px;font-weight:700">Free Estimate</a>

<!-- Welcome -->
<div class="water-panel" style="left:0;top:721px;width:505px;height:571px;clip-path:polygon(0 0,100% 0,280px 100%,0 100%)" role="img" aria-label="Blue pool water texture"></div>
<div class="diamond" style="left:149px;top:820px" role="img" aria-label="Pool technician standing beside a tiled pool"></div>
<h2 class="heading" style="left:600px;top:775px;width:534px"><span class="lead">Welcome to</span><br>Crestline Pools</h2>
<div class="copy" style="left:625px;top:866px;width:484px">
  <p>Founded in 2015, our company brings more than 18 years of hands-on experience in both commercial and residential pool service. Our team includes Certified Pool Operator (CPO) professionals who understand the highest standards of water quality, safety, and compliance.</p>
  <p>While we proudly serve residential clients, we specialize in commercial pool service, repairs, health department permitting, and state boiler permits. From routine maintenance to complex regulatory requirements, we ensure your facility operates safely, efficiently, and up to code.</p>
</div>
<a class="btn" style="left:767px;top:1161px">Read More</a>

<!-- Pool services -->
<div class="accent" style="left:419px;top:1582px"></div>
<div class="photo" style="left:434px;top:1292px;width:766px;height:398px;background:linear-gradient(180deg,#3f6b3a 0%,#4f7a46 25%,#2a9fd0 45%,#1d88c4 70%,#c9c3b8 88%)" role="img" aria-label="Technician servicing a pool cleaner at the pool edge"></div>
<h2 class="heading" style="left:40px;top:1376px;width:400px">Pools Services</h2>
<div class="copy" style="left:70px;top:1424px;width:340px">
  <p>When you invested in your pool, you knew it was a long-term investment in both money and time. At home, it's an oasis, a place to beat the heat and relax.</p>
</div>
<a class="btn" style="left:143px;top:1550px">Read More</a>

<!-- Residential -->
<div class="accent" style="left:657px;top:2024px;background:linear-gradient(315deg,var(--blue) 0 50%,var(--orange) 50% 100%)"></div>
<div class="photo" style="left:0;top:1733px;width:766px;height:401px;background:linear-gradient(180deg,#6d8aa5 0%,#b3a58a 35%,#8a7a62 52%,#1b2a4c 70%,#13203f 100%)" role="img" aria-label="Residential home with a lit pool at dusk"></div>
<h2 class="heading" style="left:780px;top:1734px;width:360px">Residential<br>Pools</h2>
<div class="copy" style="left:795px;top:1822px;width:330px;font-size:14px;line-height:24px">
  <p>Your pool should be a place to relax — not another chore on your to-do list. Our residential pool service is designed to keep your water crystal clear, balanced, and swim-ready all season long.</p>
  <p>With more than 18 years of hands-on experience, our trained professionals handle everything from routine cleaning and chemical balancing to equipment inspections and equipment repairs.</p>
</div>
<a class="btn" style="left:864px;top:2082px">Read More</a>

<!-- Commercial -->
<div class="accent" style="left:419px;top:2467px"></div>
<div class="photo" style="left:434px;top:2175px;width:766px;height:401px;background:linear-gradient(180deg,#8fb6cf 0%,#4b7d3f 25%,#3b6a36 42%,#2e78ad 60%,#1f4f8a 100%)" role="img" aria-label="Resort pool lined with palm trees and umbrellas"></div>
<h2 class="heading" style="left:40px;top:2182px;width:400px">Commercial<br>Pools</h2>
<div class="copy" style="left:75px;top:2274px;width:330px;font-size:14px;line-height:24px">
  <p>Our team includes Certified Pool Operator (CPO) professionals who specialize in commercial service, equipment repairs, and regulatory compliance.</p>
  <p>We work closely with property managers, HOA boards, hotels, and apartment communities to handle health department permits, state boiler permits, inspections, and ongoing maintenance.</p>
</div>
<a class="btn" style="left:143px;top:2522px">Read More</a>

<!-- Why choose us -->
<div class="water-panel" style="left:749px;top:2576px;width:451px;height:569px;clip-path:polygon(0 0,100% 0,100% 100%,187px 100%)" role="img" aria-label="Blue pool water texture"></div>
<div class="diamond" style="left:689px;top:2674px;background:linear-gradient(135deg,#c9b46a,#6e8a9a 55%,#3b6fa0)" role="img" aria-label="Two technicians working on pool equipment"></div>
<h2 class="heading" style="left:80px;top:2675px;width:500px"><span class="lead">Why Choose Us?</span><br>Crestline Pools</h2>
<div class="copy" style="left:75px;top:2768px;width:510px">
  <p>Choosing the right pool service company isn't just about clean water — it's about trust, reliability, and protecting your investment. Since 2015, we've built our reputation on delivering consistent, professional service backed by more than 18 years of industry experience. Our team includes Certified Pool Operator (CPO) professionals who understand water chemistry, equipment systems, and — most importantly — compliance.</p>
</div>
<a class="btn" style="left:233px;top:2980px;text-transform:none">Contact Us</a>

<!-- Client cards -->
<div class="accent" style="left:62px;top:3510px"></div>
<div class="photo" style="left:75px;top:3222px;width:511px;height:400px;background:linear-gradient(180deg,#4d8fd0 0%,#8dbde0 35%,#4b7a4a 48%,#2fb8d4 62%,#1ba3c9 100%)" role="img" aria-label="Hotel pool with palm trees under a blue sky"></div>
<div class="accent" style="left:1020px;top:3205px;background:linear-gradient(315deg,var(--blue) 0 50%,var(--orange) 50% 100%)"></div>
<div class="photo" style="left:616px;top:3222px;width:511px;height:400px;background:linear-gradient(180deg,#6c8a4a 0%,#3d6a36 35%,#27a7dc 60%,#1d8ccc 85%,#a9a59c 100%)" role="img" aria-label="Backyard freeform pool with landscaping"></div>
<h2 class="heading" style="left:75px;top:3654px;width:511px">Commercial<br>Clients Trust Us</h2>
<div class="copy" style="left:75px;top:3747px;width:511px;font-size:14px;line-height:24px">
  <p>HOAs, hotels, and apartment communities rely on us because we understand that your pool is both an amenity and a liability. We specialize in commercial service, equipment repairs.</p>
</div>
<a class="btn" style="left:234px;top:3842px">Read More</a>
<h2 class="heading" style="left:616px;top:3654px;width:511px">Homeowners<br>Count On Us</h2>
<div class="copy" style="left:621px;top:3747px;width:501px;font-size:14px;line-height:24px">
  <p>For residential customers, we make pool ownership easy. We show up on time, communicate clearly, and keep your pool swim-ready without the hassle.</p>
</div>
<a class="btn" style="left:775px;top:3842px">Read More</a>

<!-- Quick contact -->
<section class="contact" role="img" aria-label="Pool and house at night, darkened"></section>
<h2 class="abs" style="left:0;top:4012px;width:1200px;text-align:center;color:var(--white);font-weight:400;font-size:38px">Quick Contact Us</h2>
<div class="contact-line">
  <span><svg width="18" height="18" viewBox="0 0 24 24" fill="#f7941d"><path d="M6.6 10.8a15.1 15.1 0 0 0 6.6 6.6l2.2-2.2a1 1 0 0 1 1-.25 11.4 11.4 0 0 0 3.6.57 1 1 0 0 1 1 1V20a1 1 0 0 1-1 1A17 17 0 0 1 3 4a1 1 0 0 1 1-1h3.5a1 1 0 0 1 1 1c0 1.25.2 2.45.57 3.57a1 1 0 0 1-.25 1z"/></svg>(555) 014-2290</span>
  <span><svg width="18" height="14" viewBox="0 0 24 18" fill="#f7941d"><path d="M0 2a2 2 0 0 1 2-2h20a2 2 0 0 1 2 2v.3L12 9.5 0 2.3zM0 4.6l12 7.2 12-7.2V16a2 2 0 0 1-2 2H2a2 2 0 0 1-2-2z"/></svg>poolsolutions@crestlinepoolsqv.com</span>
</div>
<div class="field" style="left:165px;top:4128px;width:427px">Name</div>
<div class="field" style="left:608px;top:4128px;width:427px">Email Address</div>
<div class="field" style="left:165px;top:4191px;width:427px">Phone No</div>
<div class="field" style="left:608px;top:4191px;width:427px">Subject</div>
<div class="field message" style="left:165px;top:4259px;width:870px">Message</div>
<a class="btn" style="left:503px;top:4388px;width:195px;height:50px;text-transform:none;font-size:16px">Submit</a>

<!-- Footer -->
<nav class="footer-nav" style="left:84px"><a>Home</a><a>About Us</a><a>Services</a></nav>
<div class="brand" style="left:512px;top:4598px;color:var(--blue)"><span class="dot"></span>Crestline Pools</div>
<nav class="footer-nav" style="left:765px"><a>Why Us</a><a>Contact Us</a><a>Free Estimate</a></nav>
<p class="abs" style="left:0;top:4703px;width:1200px;text-align:center;font-size:14px;color:#333">©2026 Crestline Pools - All rights reserved.</p>
<div class="social"><span aria-label="Social link"></span><span aria-label="Social link"></span><span aria-label="Social link"></span><span aria-label="Social link"></span><span aria-label="Social link"></span></div>

</body>
</html>
```